New York City Sponsorship Page with Click Through Supporting Pages

Metro Talent Guild, the leading New York City resource for HR Professionals is a membership organization with almost 2,000 individual members.

We need section/page(s) created for our current sponsorship offerings. Our platform is on ClubNest Suite Platform and we need capability to edit the page, etc. It must be HTML ready/coded.

Attached is the mock up of how we want the page to look (pages mockup pdf) as well as each of the categories which should be included (in the excel files). Our current page is here: http://www.metrotalentguild.example/?page=sponsors and is not easy to read through. We want something that is visually appealing and clean but showcases all of the different ways to sponsor the Chapter.

Additionally, we are taking the information from this page and turning it into a brochure.

Target Market(s)

New York City Companies who have HR Professionals or services they want to attract or offer.

Coding

Coded - Design and coding required

Number of Pages Required

5+ page

Requirements
Must have
• Clean Look and feel, easy functionality, necessary information and purchases. Match the top navigation of current page. Opportunity for current sponsor logos to be highlighted on the page. Easy to update/maintain.
Nice to have
• Option to pay for sponsorships through the page using our credit card processor.
Should not have
• Overwhelming text in sections

```html
<!DOCTYPE html>
<html lang="en">
<head>
<meta charset="utf-8">
<title>Invitation for Sponsors – Metro Talent Guild</title>
<link rel="stylesheet" href="https://fonts.googleapis.com/css2?family=Roboto+Condensed:wght@300;400;700&family=Arimo:wght@400;700&display=swap">
<style>
:root{
  --navy:#0b2740;
  --nav-blue:#1a8fd0;
  --band:#e9eaec;
  --red:#a92a1a;
  --card-teal:#1a5f8e;
  --card-teal-dark:#0f4a72;
  --card-blue:#1a8fde;
  --card-blue-dark:#0b78c9;
  --card-red:#b22d16;
  --card-red-dark:#98240f;
  --card-grey:#3a3d41;
  --card-grey-dark:#2b2e31;
  --text:#1c1c1c;
  --link:#1273b9;
  --social:#1a8fd0;
  --rule:#555;
}
*{box-sizing:border-box;margin:0;padding:0}
html,body{width:1150px;height:1200px;overflow:hidden;background:#fff;font-family:"Arimo",Arial,sans-serif;color:var(--text)}
.page{position:relative;width:1150px;height:1200px}
.topbar{position:absolute;top:0;left:0;width:100%;height:24px;background:var(--navy)}
.topbar .links{position:absolute;left:600px;top:7px;display:flex;gap:11px;font-size:8px;font-weight:700;color:#fff;letter-spacing:.2px}
.search{position:absolute;left:757px;top:5px;width:108px;height:15px;background:#fff;border-radius:2px;font-size:7px;color:#999;padding:4px 5px}
.search svg{position:absolute;right:4px;top:3px}
.social-row{position:absolute;left:871px;top:5px;display:flex;gap:5px}
.social-row span,.connect .icons span{display:block;background:var(--social);border-radius:2px}
.social-row span{width:15px;height:15px}
.navband{position:absolute;top:24px;left:0;width:100%;height:58px;background:var(--band)}
.brand{position:absolute;left:184px;top:18px;display:flex;align-items:center;gap:6px;font-family:"Roboto Condensed",sans-serif;font-weight:700;font-size:17px;color:var(--red)}
.brand i{display:block;width:14px;height:14px;border-radius:50%;background:var(--navy)}
.mainnav{position:absolute;left:425px;top:22px;display:flex;gap:23px;font-family:"Roboto Condensed",sans-serif;font-size:13px;color:var(--nav-blue)}
.hero{position:absolute;top:82px;left:0;width:100%;height:105px;background:linear-gradient(180deg,#1b2230 0%,#3a3d48 45%,#5a4d3a 75%,#2a2a2e 100%)}
.content{position:absolute;left:183px;top:0;width:820px}
h1{position:absolute;top:214px;left:0;font-family:"Roboto Condensed",sans-serif;font-weight:400;font-size:27px;color:var(--red);white-space:nowrap}
.crumbs{position:absolute;top:259px;left:0;font-size:8.5px;color:#333;white-space:nowrap}
.share{position:absolute;top:286px;left:0;display:flex;align-items:center;gap:3px;font-size:10px;color:var(--red)}
.share b{display:inline-block;width:10px;height:10px;background:#e04a2d}
.share em{font-style:normal;color:#333;margin:0 4px}
.share span{display:inline-block;width:10px;height:10px;background:#3b6db4}
.share span.r{background:#c8232c}.share span.m{background:#d54b3d}
.intro{position:absolute;top:314px;left:1px;font-size:10px;line-height:24.5px;white-space:nowrap}
.cards{position:absolute;top:409px;left:1px;display:flex;gap:10px}
.card{width:154px;height:222px;color:#fff;text-align:center}
.card .head{height:115px;position:relative}
.card .icon{position:absolute;left:53px;top:11px;width:49px;height:49px;border-radius:50%;background:#fff;display:flex;align-items:center;justify-content:center}
.card h2{position:absolute;top:67px;left:0;width:100%;font-family:"Roboto Condensed",sans-serif;font-weight:400;font-size:17px;line-height:17px}
.card h2.one{top:76px}
.card .body{height:107px;padding:12px 9px 0;font-size:10px;line-height:12.3px;position:relative}
.card .price{position:absolute;bottom:14px;left:0;width:100%;font-family:"Roboto Condensed",sans-serif;font-weight:700;font-size:18px}
.c1 .head{background:var(--card-teal)}.c1 .body{background:var(--card-teal-dark)}
.c2 .head{background:var(--card-blue)}.c2 .body{background:var(--card-blue-dark)}
.c3 .head{background:var(--card-red)}.c3 .body{background:var(--card-red-dark)}
.c4 .head{background:var(--card-grey)}.c4 .body{background:var(--card-grey-dark)}
.actions{position:absolute;top:667px;left:0;font-size:10px;line-height:24.3px}
.actions div{display:flex;align-items:center;gap:5px}
.actions .more{color:var(--link)}.actions .book{color:#c00}
.rule{position:absolute;left:0;width:330px;height:1px;background:var(--rule)}
.sponsors{position:absolute;top:776px;left:1px;font-size:10px}
.tier{font-weight:700;margin-top:7px}
.logos{display:flex;gap:40px;align-items:center;height:38px;font-family:"Arimo",sans-serif;font-weight:700;font-size:17px;color:#1d4f9c;white-space:nowrap}
.logos.silver{color:#1d5ea8}
.footer{position:absolute;top:980px;left:0;width:100%;height:220px;background:var(--navy);color:#fff}
.fcol{position:absolute;top:28px}
.fcol h3{font-family:"Roboto Condensed",sans-serif;font-weight:300;font-size:16px;margin-bottom:8px}
.fcol ul{list-style:none;font-size:8.5px;line-height:16px}
.fcol.contact ul{line-height:23.3px}
.badge{position:absolute;left:542px;top:38px;width:142px;height:99px;background:#fff;padding:3px}
.badge div{width:100%;height:100%;background:linear-gradient(180deg,#5b8fc9,#2f64a6)}
.connect .icons{display:flex;gap:8px;margin-top:4px}
.connect .icons span{width:25px;height:25px}
.legal{position:absolute;top:196px;left:0;width:100%;text-align:center;font-size:7.5px}
</style>
</head>
<body>
<div class="page">
  <header>
    <div class="topbar">
      <div class="links"><span>CONTACT US</span><span>SIGN IN</span><span>JOIN/RENEW</span></div>
      <div class="search">Enter search criteria...
        <svg width="8" height="8" viewBox="0 0 10 10"><circle cx="4" cy="4" r="3" fill="none" stroke="#1a8fd0" stroke-width="1.5"/><path d="M6 6l3 3" stroke="#1a8fd0" stroke-width="1.5"/></svg>
      </div>
      <div class="social-row" aria-label="Social links"><span></span><span></span><span></span><span></span><span></span></div>
    </div>
    <div class="navband">
      <div class="brand"><i></i>Metro Talent Guild</div>
      <nav class="mainnav"><span>Our New Website</span><span>About Us</span><span>Membership</span><span>Events</span><span>Sponsorships</span><span>Career Center</span><span>HR Resources</span></nav>
    </div>
    <div class="hero" role="img" aria-label="Night skyline of Manhattan with lit office towers"></div>
  </header>

  <main class="content">
    <h1>Invitation for Sponsors</h1>
    <div class="crumbs">Sponsorships &nbsp;» Sponsorship Opportunitiers</div>
    <div class="share"><b></b>Share<em>|</em><span></span><span></span><span class="r"></span><span class="m"></span></div>
    <div class="intro">
      <p>Thank you for your nterest in Metro Talent Guild.</p>
      <p>As a premier Talent Society chapter, we offer many oportunities to increase your exposure to the New York City HR community.</p>
      <p>Choose the sponsorship category that best meets your needs:</p>
    </div>

    <section class="cards">
      <article class="card c1">
        <div class="head">
          <div class="icon"><svg width="22" height="22" viewBox="0 0 24 24" fill="none" stroke="#0f4a72" stroke-width="1.8"><path d="M12 3a6 6 0 0 0-3.5 10.9V17h7v-3.1A6 6 0 0 0 12 3z"/><path d="M9.5 20h5M10.5 22h3M12 10v5"/></svg></div>
          <h2>Strategic<br>Partnership</h2>
        </div>
        <div class="body">Opportunities for a strategic sponsorship at different levels, each providing a valuable set of great benefits<div class="price">$3,500+</div></div>
      </article>
      <article class="card c2">
        <div class="head">
          <div class="icon"><svg width="28" height="22" viewBox="0 0 28 22" fill="none" stroke="#0b78c9" stroke-width="1.6"><circle cx="14" cy="6" r="3"/><circle cx="6" cy="8" r="2.5"/><circle cx="22" cy="8" r="2.5"/><path d="M8 19v-3a6 6 0 0 1 12 0v3zM2 19v-2a4 4 0 0 1 5-3.8M26 19v-2a4 4 0 0 0-5-3.8"/></svg></div>
          <h2>Programs<br>/ Events</h2>
        </div>
        <div class="body">Opportunities to sponsor a wide range of events like all-day conference, 2 hour sessions etc.<div class="price">$500+</div></div>
      </article>
      <article class="card c3">
        <div class="head">
          <div class="icon"><svg width="26" height="20" viewBox="0 0 26 20" fill="none" stroke="#98240f" stroke-width="1.8"><rect x="4" y="3" width="18" height="11" rx="1"/><path d="M1 17h24"/></svg></div>
          <h2>Advertising<br>/ Promotion</h2>
        </div>
        <div class="body">Opportunities for regular or one time digital sponsoring in form of website banners, website ads, e-blasts etc.<div class="price">$150+</div></div>
      </article>
      <article class="card c4">
        <div class="head">
          <div class="icon"><svg width="22" height="22" viewBox="0 0 24 24" fill="none" stroke="#2b2e31" stroke-width="1.8"><circle cx="12" cy="12" r="3.2"/><path d="M12 2.5v3M12 18.5v3M2.5 12h3M18.5 12h3M5.3 5.3l2.1 2.1M16.6 16.6l2.1 2.1M5.3 18.7l2.1-2.1M16.6 7.4l2.1-2.1"/><circle cx="12" cy="12" r="6.5"/></svg></div>
          <h2 class="one">Custom</h2>
        </div>
        <div class="body">Build your own sponsorship program from our variety of opportunities<div class="price">$250+</div></div>
      </article>
    </section>

    <div class="actions">
      <div class="more"><svg width="10" height="9" viewBox="0 0 10 9"><path d="M1 1l4 3 4-3M1 5l4 3 4-3" fill="none" stroke="#1273b9" stroke-width="1.6"/></svg>More about our sponsorship packages</div>
      <div class="book"><svg width="10" height="9" viewBox="0 0 10 9"><path d="M2 1h7L8 8H1z" fill="#c00"/></svg>Book your sponsorship package</div>
      <div><svg width="11" height="8" viewBox="0 0 11 8"><rect width="11" height="8" fill="#333"/><path d="M0 0l5.5 4L11 0" fill="none" stroke="#fff" stroke-width="1"/></svg>Contact our sponsorship team</div>
    </div>

    <div class="rule" style="top:758px"></div>
    <section class="sponsors">
      <p>Thanks to our Sponsors</p>
      <p class="tier">Gold</p>
      <div class="logos"><span>Harlow &amp; Pike</span><span>TransitPerk Solutions</span></div>
      <p class="tier" style="margin-top:0">Silver</p>
      <div class="logos silver"><span>Beacon Benefits Group</span><span>Staffwell</span></div>
    </section>
    <div class="rule" style="top:939px"></div>
  </main>

  <footer class="footer">
    <div class="fcol" style="left:238px"><h3>Navigation</h3>
      <ul><li>About Us</li><li>Membership</li><li>Events</li><li>Career Center</li><li>Sponsorships</li><li>HR Resources</li></ul></div>
    <div class="fcol contact" style="left:373px"><h3>Contact Us</h3>
      <ul><li>Phone: 555-010-4769</li><li>Fax: 555-010-8244</li><li>info@metrotalentguild.example</li></ul></div>
    <div class="badge" aria-label="Affiliate badge"><div></div></div>
    <div class="fcol connect" style="left:753px"><h3>Connect With Us</h3>
      <div class="icons"><span></span><span></span><span></span><span></span><span></span></div></div>
    <div class="legal">Membership Software Powered by ClubNest Suite® &nbsp;:: &nbsp;Legal</div>
  </footer>
</div>
</body>
</html>
```